Helpdesk Brochure

Would like to revamp an old brochure for a conference
Can I please add our 1300 857 619 in the footer
Printing this on a double sided Brochure

```html
<!DOCTYPE html>
<html lang="en">
<head>
<meta charset="utf-8">
<title>Corvana – IT Support Brochure</title>
<link rel="stylesheet" href="https://fonts.googleapis.com/css2?family=Montserrat:wght@400;500;700;800;900&family=Poppins:wght@800;900&display=swap">
<style>
  :root {
    --orange: #e3891f;
    --orange-light: #f6a944;
    --orange-deep: #d67d17;
    --grey-light: #ececec;
    --charcoal: #2a2a2a;
    --ink: #262626;
    --white: #ffffff;
    --shadow-brown: #8a4f12;
  }
  html, body { margin: 0; padding: 0; overflow: hidden; background: var(--white); }
  .brochure {
    position: relative; width: 856px; height: 1200px; overflow: hidden;
    background: var(--white); font-family: "Montserrat", sans-serif;
  }
  .backdrop { position: absolute; inset: 0; }
  .hero-title {
    position: absolute; left: 443px; top: 184px; margin: 0; text-align: left;
    font-family: "Poppins", sans-serif; font-weight: 900; color: var(--white);
    letter-spacing: -2px; white-space: nowrap;
    text-shadow: 4px 4px 0 var(--shadow-brown);
  }
  .hero-title span { display: block; }
  .hero-title .line-city { font-size: 62px; line-height: 50px; }
  .hero-title .line-leading { font-size: 89px; line-height: 58px; letter-spacing: -3px; }
  .hero-title .line-support { font-size: 69px; line-height: 86px; letter-spacing: -2.5px; }
  .hero-lede {
    position: absolute; right: 34px; top: 371px; width: 380px; text-align: right; color: var(--white);
  }
  .hero-lede h2 {
    margin: 0 0 1px; font-family: "Poppins", sans-serif; font-weight: 800; font-size: 17.5px;
    line-height: 1.1; text-shadow: 1px 1px 0 var(--shadow-brown); letter-spacing: 0.1px;
  }
  .hero-lede p { margin: 0; font-size: 14.2px; line-height: 1.22; font-weight: 500; }
  .brand {
    position: absolute; left: 25px; top: 420px; color: var(--white);
  }
  .brand-name {
    display: flex; align-items: center; gap: 9px;
    font-size: 36px; font-weight: 800; letter-spacing: 2px; line-height: 1;
  }
  .brand-dot { width: 16px; height: 16px; border-radius: 50%; background: var(--white); }
  .brand-tag { margin-top: 10px; font-size: 6.2px; letter-spacing: 1.1px; font-weight: 500; }
  .offer-title {
    position: absolute; left: 34px; top: 640px; margin: 0;
    font-weight: 800; font-size: 47px; line-height: 0.98; color: var(--charcoal); letter-spacing: -0.5px;
  }
  .offer-title span { display: block; }
  .offer-title .accent { color: var(--orange); font-size: 56.5px; font-weight: 900; }
  .services { position: absolute; left: 446px; top: 532px; width: 380px; margin: 0; padding: 0; list-style: none; }
  .service { margin-bottom: 5px; }
  .service-icon {
    width: 40px; height: 40px; border-radius: 50%; background: var(--orange);
    display: flex; align-items: center; justify-content: center;
  }
  .service h3 { margin: 5px 0 5px; font-weight: 800; font-size: 20.5px; line-height: 1.2; color: var(--ink); }
  .service p { margin: 0; font-size: 12.4px; line-height: 1.2; color: var(--orange); font-weight: 500; }
  .contact { position: absolute; left: 27px; top: 1040px; color: var(--white); }
  .contact .cta { margin: 0; font-size: 39px; font-weight: 500; letter-spacing: 0.5px; line-height: 1; }
  .contact .phone {
    margin: 6px 0 0; font-family: "Poppins", sans-serif; font-weight: 900; font-size: 66px; line-height: 1; letter-spacing: 4px;
  }
  .contact .web { margin: 6px 0 0 3px; font-family: "Poppins", sans-serif; font-weight: 800; font-size: 21px; letter-spacing: 0.6px; }
</style>
</head>
<body>
<main class="brochure">
  <svg class="backdrop" width="856" height="1200" viewBox="0 0 856 1200">
    <defs>
      <linearGradient id="photoTone" x1="0" y1="0" x2="1" y2="1">
        <stop offset="0" stop-color="#3d4650"/>
        <stop offset="0.45" stop-color="#4c555d"/>
        <stop offset="1" stop-color="#2f2a27"/>
      </linearGradient>
      <radialGradient id="photoGlow" cx="0.35" cy="0.55" r="0.35">
        <stop offset="0" stop-color="#f0b060" stop-opacity="0.55"/>
        <stop offset="1" stop-color="#f0b060" stop-opacity="0"/>
      </radialGradient>
    </defs>
    <g class="hero-photo" role="img" aria-label="Photo of a businessman working on a laptop with a glowing globe and support keywords over a background of code">
      <polygon points="0,0 780,0 393,343 522,437 330,520 250,560 0,470" fill="url(#photoTone)"/>
      <polygon points="0,0 780,0 393,343 522,437 330,520 250,560 0,470" fill="url(#photoGlow)"/>
    </g>
    <polygon class="band-orange" points="0,430 250,560 330,520 522,437 450,500 330,555 245,580 140,540 0,645" fill="var(--orange)"/>
    <polygon class="band-orange" points="780,0 856,0 856,690 522,437 393,343" fill="var(--orange)"/>
    <polygon class="band-orange-light" points="723,16 723,477 393,343" fill="var(--orange-light)"/>
    <polygon class="band-orange" points="0,265 250,455 0,640" fill="var(--orange)"/>
    <polygon class="panel-grey" points="0,645 142,537 243,578 321,537 422,748 319,996 0,820" fill="var(--grey-light)"/>
    <polygon class="band-orange" points="0,820 319,996 559,1128 464,1200 0,1200" fill="var(--orange)"/>
    <polygon class="corner-dark" points="464,1200 695,1030 856,1096 856,1200" fill="var(--charcoal)"/>
    <polygon class="corner-dark-facet" points="695,1030 856,1096 760,1140" fill="#3a3a3a"/>
  </svg>

  <h1 class="hero-title">
    <span class="line-city">MELBURNE’S</span>
    <span class="line-leading">LEADING</span>
    <span class="line-support">IT SUPPORT</span>
  </h1>

  <div class="hero-lede">
    <h2>TAKING CARE OF YOUR IT HEADACHES</h2>
    <p>We partner with all types of businesses to solve<br>their IT problems with continuous ongoing<br>support and solutions that work.</p>
  </div>

  <div class="brand">
    <div class="brand-name"><span class="brand-dot"></span>CORVANA</div>
    <div class="brand-tag">SMART TECHNOLOGY FOR GROWING BUSINESSES</div>
  </div>

  <h2 class="offer-title">
    <span>CLOUD</span>
    <span>PHONE</span>
    <span>SYSTEMS</span>
    <span class="accent">&amp; INTERNET</span>
  </h2>

  <ul class="services">
    <li class="service">
      <div class="service-icon">
        <svg width="22" height="22" viewBox="0 0 24 24" fill="#fff"><path d="M6.6 10.8a15 15 0 0 0 6.6 6.6l2.2-2.2a1 1 0 0 1 1-.25 11.4 11.4 0 0 0 3.6.57 1 1 0 0 1 1 1V20a1 1 0 0 1-1 1A17 17 0 0 1 3 4a1 1 0 0 1 1-1h3.5a1 1 0 0 1 1 1c0 1.25.2 2.45.57 3.57a1 1 0 0 1-.25 1z"/></svg>
      </div>
      <h3>VoIP &amp; Phone Systems</h3>
      <p>We provide expert services in installation VoIP<br>and communications hardware and systems.</p>
    </li>
    <li class="service">
      <div class="service-icon">
        <svg width="24" height="24" viewBox="0 0 24 24" fill="#fff"><circle cx="12" cy="7" r="3"/><circle cx="5.5" cy="9" r="2.2"/><circle cx="18.5" cy="9" r="2.2"/><path d="M6.5 18a5.5 5.5 0 0 1 11 0zM1 18a4.5 4.5 0 0 1 5.2-4.4A6.5 6.5 0 0 0 5 18zM23 18a4.5 4.5 0 0 0-5.2-4.4A6.5 6.5 0 0 1 19 18z"/></svg>
      </div>
      <h3>TeamLink Calling</h3>
      <p>Experience the next level of collaboration with our<br>TeamLink calling services, empowering your<br>team with seamless communication and features.</p>
    </li>
    <li class="service">
      <div class="service-icon">
        <svg width="22" height="22" viewBox="0 0 24 24"><path d="M3 4h18v12H9l-4 4v-4H3z" fill="#fff"/><path d="M7 8h10M7 11h10M7 14h6" stroke="var(--orange)" stroke-width="1.5"/></svg>
      </div>
      <h3>SMS Gateway</h3>
      <p>Unlock seamless communication with our cutting-edge<br>SMS Gateway services, ensuring instant and reliable<br>message delivery for your business needs.</p>
    </li>
    <li class="service">
      <div class="service-icon">
        <svg width="24" height="24" viewBox="0 0 24 24" fill="none" stroke="#fff" stroke-width="2.2" stroke-linecap="round"><path d="M3 9.5a13 13 0 0 1 18 0M6 12.8a8.5 8.5 0 0 1 12 0M9 16a4 4 0 0 1 6 0"/><circle cx="12" cy="19" r="1.2" fill="#fff"/></svg>
      </div>
      <h3>Broadband, Fibre &amp; 4G Internet</h3>
      <p>Stay connected, delivering reliable and high-speed<br>connectivity tailored to your business requirements.</p>
    </li>
  </ul>

  <div class="contact">
    <p class="cta">CALL NOW</p>
    <p class="phone">1300 857 619</p>
    <p class="web">www.corvanacomputers.com.au</p>
  </div>
</main>
</body>
</html>
```